Design a book cover
TItle: Where Does Mercy Sleep?
Suggested graphic: Jesus holding a gun
Subtitle: A public defender's views on the death penalty
Author Name: Norbert Kestelman

```html
<!DOCTYPE html>
<html lang="en">
<head>
<meta charset="UTF-8">
<title>Where Does Mercy Sleep? — Book Cover</title>
<link href="https://fonts.googleapis.com/css2?family=Playfair+Display:wght@900&family=Montserrat:wght@400&family=Oswald:wght@400&display=swap" rel="stylesheet">
<style>
  :root {
    --stage: #e8e5de;
    --paper: #f3eedd;
    --ink: #111111;
    --crimson: #b8212a;
    --rule: #3a3a3a;
    --art-tone: #e2ddcc;
  }
  * { margin: 0; padding: 0; box-sizing: border-box; }
  html, body {
    width: 1200px;
    height: 730px;
    overflow: hidden;
    background: var(--stage);
  }
  .stage {
    position: relative;
    width: 1200px;
    height: 730px;
    display: flex;
    align-items: center;
    justify-content: center;
  }
  .cover {
    position: relative;
    width: 466px;
    height: 700px;
    background: var(--paper);
    overflow: hidden;
  }
  .subtitle {
    position: absolute;
    left: 150px;
    top: 82px;
    padding-left: 12px;
    border-left: 1.5px solid var(--rule);
    font-family: 'Montserrat', sans-serif;
    font-size: 14px;
    line-height: 1.22;
    color: var(--ink);
  }
  .cover-art {
    position: absolute;
    left: 292px;
    top: 70px;
    width: 96px;
    height: 160px;
  }
  .title {
    position: absolute;
    right: 38px;
    top: 220px;
    text-align: right;
    font-family: 'Playfair Display', serif;
    font-weight: 900;
    line-height: 0.86;
    letter-spacing: -0.02em;
  }
  .title span { display: block; }
  .title .dark { color: var(--ink); font-size: 92px; }
  .title .red { color: var(--crimson); font-size: 96px; }
  .author {
    position: absolute;
    left: 0;
    right: 0;
    top: 604px;
    text-align: center;
    font-family: 'Oswald', sans-serif;
    font-size: 24px;
    letter-spacing: 0.2em;
    color: var(--ink);
  }
</style>
</head>
<body>
  <main class="stage">
    <article class="cover">
      <p class="subtitle">A public<br>defender's<br>views on<br>the death<br>penalty</p>
      <svg class="cover-art" viewBox="0 0 96 160" role="img" aria-label="Line drawing of a hand holding a revolver pointed at the viewer">
        <rect width="96" height="160" rx="6" fill="var(--art-tone)"/>
      </svg>
      <h1 class="title">
        <span class="dark">Where</span>
        <span class="dark">Does</span>
        <span class="red">Mercy</span>
        <span class="red">Sleep?</span>
      </h1>
      <p class="author">NORBERT KESTELMAN</p>
    </article>
  </main>
</body>
</html>
```